Brochure for real estate company

We need the brochure in the attachement re-designed in a consistent way with our website. The text and the structure of the text should not be altered, but addidtional design-elements and other stuff can be added. We're looking for a simple and catchy design as in our website (www.lerchfeld-wohnbau.ch). We need design propositions in file formats where we can always change the text ourselves if that is neccessary later on.

Industry/Entity Type

Real Estate

Font styles to use
Sans Serif

Colors
ec2027
f04a50

```html
<!DOCTYPE html>
<html lang="de">
<head>
<meta charset="utf-8">
<title>Broschüre – Dokumentation &amp; Insertion</title>
<link rel="stylesheet" href="https://fonts.googleapis.com/css2?family=Open+Sans:ital,wght@0,400;0,700;0,800;1,400;1,600&display=swap">
<style>
  :root{
    --red:#ec2027;
    --red-soft:#f04a50;
    --red-deep:#b8161c;
    --black:#1a1a1a;
    --yellow:#f6d33c;
    --white:#ffffff;
    --grey:#6d6d6d;
    --wood:#a0582a;
    --wood-light:#d08a4c;
    --green:#5e8c3a;
  }
  *{margin:0;padding:0;box-sizing:border-box}
  html,body{width:1200px;height:300px;overflow:hidden;background:var(--white)}
  body{font-family:"Open Sans",Arial,sans-serif;position:relative}
  .panel{position:absolute;top:0;height:300px;overflow:hidden}
  .abs{position:absolute}

  /* Panel 1 */
  .panel-docs{left:0;width:250px;background:var(--red)}
  .title-disc{left:-10px;top:-6px;width:104px;height:104px;border-radius:50%;background:var(--black);
    color:var(--white);font-weight:800;font-size:9.6px;line-height:11.5px;letter-spacing:-.2px;
    display:flex;align-items:center;justify-content:center;text-align:center;padding-left:10px;padding-top:6px}
  .intro{left:94px;top:62px;width:150px;color:var(--yellow);font-style:italic;font-size:6.2px;line-height:8px}
  .bullets{list-style:none;font-size:5.4px;line-height:7px;color:var(--white)}
  .bullets li{position:relative;padding-left:7px;margin-bottom:2px}
  .bullets li::before{content:"";position:absolute;left:0;top:2.5px;width:3px;height:3px;border-radius:50%;background:currentColor}
  .bullets .hl{color:var(--yellow)}
  .docs-list{left:14px;top:98px;width:226px}
  .why-box{left:0;top:140px;width:250px;height:160px;background:var(--red-deep)}
  .why-title{left:10px;top:146px;width:235px;color:var(--yellow);font-weight:700;font-size:8.2px}
  .why-cols{left:10px;top:162px;width:232px;display:flex;gap:10px;color:var(--white);font-size:5.2px;line-height:6.8px}
  .why-cols p{flex:1}

  /* Panel 2 */
  .panel-portfolio{left:250px;width:250px;background:var(--white)}
  .hero-photo{left:14px;top:10px;width:226px;height:148px;background:linear-gradient(180deg,#9cc3e6 0%,#b9d4ea 40%,var(--green) 62%,#3f6b26 100%)}
  .portfolio-disc{left:-2px;top:46px;width:86px;height:86px;border-radius:50%;background:var(--red);
    color:var(--white);font-weight:800;font-size:13px;display:flex;align-items:center;justify-content:center}
  .thumb{width:64px;height:64px;border-radius:50%;top:200px}
  .thumb-a{left:22px;background:linear-gradient(180deg,#9cbfe0,#d9d3c3 55%,#6f8f4b)}
  .thumb-b{left:98px;background:linear-gradient(180deg,#8fb8de,#e5dccb 50%,#5d7f3c)}
  .thumb-c{left:172px;background:linear-gradient(180deg,#a9c8e5,#ece7dd 50%,#76905a)}

  /* Panel 3 */
  .panel-visits{left:500px;width:250px;background:var(--red)}
  .room-photo{left:6px;top:0;width:238px;height:300px;background:linear-gradient(180deg,var(--wood-light) 0%,var(--wood) 45%,#6b3818 100%)}
  .overlay-disc{left:40px;top:40px;width:240px;height:240px;border-radius:50%;background:var(--red-soft);opacity:.82}
  .visits-title{left:64px;top:62px;color:var(--white);font-style:italic;font-weight:600;font-size:12px}
  .visits-list{left:64px;top:84px;width:176px}

  /* Panel 4 */
  .panel-clear{left:750px;width:450px;background:var(--white)}
  .round-photo{left:12px;top:8px;width:76px;height:76px;border-radius:50%;background:linear-gradient(180deg,#a7c9e8,#7fae55 60%,#4d7a2c)}
  .clear-title{left:12px;top:140px;width:220px;color:var(--red);font-style:italic;font-size:14px;line-height:15px}
  .clear-list{left:12px;top:180px;width:200px;color:var(--grey)}
  .strip-photo{left:356px;top:22px;width:94px;height:278px;background:linear-gradient(180deg,#c88a55 0%,var(--wood) 50%,#7a4420 100%)}
</style>
</head>
<body>

<section class="panel panel-docs">
  <div class="abs title-disc">DOKUMENTATION<br>&amp; INSERTION</div>
  <p class="abs intro">Die Basis einer seriösen Vermittlung ist die lückenlose Darstellung. Gemeinsam beginnen wir mit dem ersten Schritt.</p>
  <ul class="abs bullets docs-list">
    <li>Verkaufsdokumentation: Wir erstellen für Sie ein ansprechendes und <span class="hl">aussagekräftiges</span> Dossier.</li>
    <li>Insertion: Wir inserieren für Sie <span class="hl">auf allen wichtigen Portalen.</span> Durch intelligenten Einsatz der Verkaufskanäle erscheint Ihr Objekt immer am richtigen Ort.</li>
    <li>Aktualität: Titel, Texte und Bilder haben <span class="hl">stets Priorität.</span></li>
  </ul>
  <div class="abs why-box"></div>
  <h2 class="abs why-title">Warum Sie ausgerechnet bei uns besser fahren</h2>
  <div class="abs why-cols">
    <p>Wir sparen nicht auf Ihre Kosten: Viele Vermittler inserieren Objekte mit nur einem oder maximal zwei Bildern auf den Immobilienplattformen. Resultat: Weniger Kosten für den Vermittler, weniger Interessenten für den Verkäufer – nicht bei uns! Wir verkaufen nur für Sie: Grosse Vermittler wollen Objekte verkaufen, gleich welches. Aus diesem Grund werden Interessenten dort immer auch automatisiert per E-Mail Vergleichsobjekte präsentiert, was die Chance verringert, dass Ihr Objekt</p>
    <p>wahrgenommen wird – bei uns sind Sie und Ihre Liegenschaft im Mittelpunkt. Wir nehmen uns Zeit: Grosse Vermittler arbeiten oft mit computergenerierten Standarddokumentationen, die sich auf maximal 2 Seiten beschränken. Wir rücken Ihre Liegenschaft durch eine individuelle Dokumentation ins richtige Licht.<br><br>Der richtige Umgang mit Menschen ist das Herzstück jeder Vermittlung. Hier richten wir ein besonderes Augenmerk.</p>
  </div>
</section>

<section class="panel panel-portfolio">
  <div class="abs hero-photo" role="img" aria-label="Foto: Haus mit Garten und Fahne unter blauem Himmel"></div>
  <div class="abs portfolio-disc">PORTFOLIO</div>
  <div class="abs thumb thumb-a" role="img" aria-label="Foto: Einfamilienhaus"></div>
  <div class="abs thumb thumb-b" role="img" aria-label="Foto: Mehrfamilienhaus mit Garten"></div>
  <div class="abs thumb thumb-c" role="img" aria-label="Foto: Wohnhaus mit weisser Fassade"></div>
</section>

<section class="panel panel-visits">
  <div class="abs room-photo" role="img" aria-label="Foto: Wohnraum mit Holzdecke und Holzboden"></div>
  <div class="abs overlay-disc"></div>
  <h2 class="abs visits-title">Besichtigungen &amp; Unterstützung</h2>
  <ul class="abs bullets visits-list">
    <li>Geschwindigkeit: Bei uns gibt es keine Wartezeiten, Interessentenanfragen beantworten wir umgehend – auch am Wochenende.</li>
    <li>Individuelle Beratung: Wir führen jede Besichtigung persönlich durch und nehmen uns Zeit für den einzelnen Käufer.</li>
    <li>Wir stehen zur Seite: Wir helfen dem potenziellen Käufer bei Fragen rund um die Finanzierung und Bankabklärungen.</li>
    <li>Wir geben Antworten: Neben einer kompetenten Beratung bieten wir eine unkomplizierte Unterstützung zu Reservations- und Kaufabwicklung.</li>
  </ul>
</section>

<section class="panel panel-clear">
  <div class="abs round-photo" role="img" aria-label="Foto: Haus im Grünen"></div>
  <h2 class="abs clear-title">Klartext: Das machen wir besser als die Konkurrenz</h2>
  <ul class="abs bullets clear-list">
    <li>Wir sind schnell: Viele Makler sind überlastet, so dass Interessentenanfragen verzögert beantwortet werden oder teilweise sogar ganz vergessen gehen. Bei uns bekommt jeder Käufer eine Antwort.</li>
    <li>Wir organisieren sinnvoll: Besichtigungen sind bei vielen Maklern an der Tagesordnung. Wir bereiten diese gezielt vor.</li>
    <li>Immobilienkäufe scheitern oft an der Finanzierung. Wir unterstützen die Käufer aktiv beim Finanzierungsprozess und fördern so einen sicheren Abschluss – damit Ihr Verkauf nicht vom Zufall abhängt.</li>
  </ul>
  <div class="abs strip-photo" role="img" aria-label="Foto: Esszimmer mit Holzbalkendecke"></div>
</section>

</body>
</html>
```